Swimming pool service business postcard redesign

We need a fresh post card design for our pool service business based in San Diego called Tide Sweepers. We are a family based, local residential pool cleaning and maintenance company. we need an offer to stand out, our logo, our colors, etc on a 5.5x8 inch full color post card.

```html
<!DOCTYPE html>
<html lang="en">
<head>
<meta charset="utf-8">
<title>Tide Sweepers – Postcard Front and Back</title>
<link href="https://fonts.googleapis.com/css2?family=Anton&family=Montserrat:wght@400;500;600;700;800&display=swap" rel="stylesheet">
<style>
:root{
  --navy:#17386e;
  --blue:#1f63b8;
  --sky:#3a9be0;
  --red:#e8412c;
  --white:#ffffff;
  --ink:#1d2a44;
  --grey:#5f6778;
  --stage:#c9c9c9;
  --panel-line:#2b4f8c;
  --note:#e6eefa;
}
*{box-sizing:border-box;margin:0;padding:0}
html,body{width:1200px;height:3121px;overflow:hidden}
body{background:var(--stage);font-family:"Montserrat",sans-serif;color:var(--ink);position:relative}
.card{position:absolute;left:189px;width:822px;height:566px;overflow:hidden;background:var(--white)}
.front{top:994px}
.back{top:1613px}

/* FRONT */
.front .scene{position:absolute;inset:0;background:linear-gradient(180deg,#2f8fd8 0%,#7cc2ee 38%,#bfe3f5 52%,#4ea7e2 62%,#1f6fc2 100%)}
.headline-bg{position:absolute;left:34px;top:30px;width:560px;height:160px;background:var(--white);border-radius:14px;opacity:.92}
.headline{position:absolute;left:44px;top:36px;font-family:"Anton",sans-serif;font-style:italic;line-height:.98;letter-spacing:1px;transform:skewX(-6deg)}
.headline span{display:block;font-size:72px}
.headline .l1{color:var(--navy)}
.headline .l2{color:var(--red)}
.tagbar{position:absolute;left:54px;top:190px;width:408px;height:32px;background:var(--red);color:var(--white);font-weight:600;font-size:15px;letter-spacing:.6px;display:flex;align-items:center;justify-content:center}
.logo{position:absolute;display:flex;align-items:center;gap:8px;font-weight:800;white-space:nowrap}
.front .logo{right:40px;top:150px;font-size:34px;color:var(--white)}
.logo .dot{width:18px;height:18px;border-radius:50%;background:var(--red);flex:none}
.mascot{position:absolute;background:linear-gradient(180deg,#f28a3a 0%,#2d6fc4 55%,#1d4e96 100%);border-radius:40% 40% 8px 8px}
.front .mascot-top{right:80px;top:12px;width:110px;height:128px}
.front .mascot-left{left:28px;top:250px;width:150px;height:162px}
.truck{position:absolute;left:432px;top:228px;width:360px;height:180px;border-radius:18px;background:linear-gradient(90deg,#e9542c 0%,#f38a3b 30%,#2f7fd2 60%,#1d4d9a 100%)}
.offer{position:absolute;left:32px;top:412px;width:140px;height:154px;background:var(--white);text-align:center;padding-top:10px}
.offer .lbl{font-size:10px;font-weight:700;color:var(--navy);line-height:1.2}
.offer .price{font-family:"Anton",sans-serif;color:var(--red);font-size:62px;line-height:1;margin-top:2px}
.offer .price sup{font-size:26px;vertical-align:top;position:relative;top:6px}
.offer .note{font-size:10px;font-weight:600;color:var(--navy);line-height:1.15;margin-top:4px}
.features{position:absolute;left:172px;top:432px;width:650px;height:86px;display:flex;background:linear-gradient(90deg,rgba(31,99,184,.92),rgba(35,110,200,.92))}
.feature{flex:1;text-align:center;color:var(--white);padding-top:4px;border-right:1px solid rgba(255,255,255,.35)}
.feature:last-child{border-right:none}
.feature .ic{width:34px;height:34px;border-radius:50%;background:var(--white);margin:0 auto 4px;display:flex;align-items:center;justify-content:center}
.feature h3{font-size:12.5px;font-weight:600}
.feature p{font-size:9px;line-height:1.25;margin-top:2px}
.footbar{position:absolute;left:0;bottom:0;width:822px;height:48px;display:flex;align-items:center;color:var(--white);background:linear-gradient(90deg,#1f63b8 0%,#2766b8 55%,#e8412c 100%)}
.front .footbar{left:172px;width:650px;padding-left:18px}
.footbar .about{font-size:8.5px;line-height:1.4;width:250px}
.contact{display:flex;align-items:center;gap:6px;font-weight:600;font-size:15px;margin-left:22px;white-space:nowrap}
.contact .ci{width:18px;height:18px;flex:none}
.front .strip{position:absolute;left:0;bottom:0;width:32px;height:48px;background:var(--sky)}

/* BACK */
.back .water{position:absolute;right:0;top:0;width:360px;height:150px;background:linear-gradient(90deg,rgba(255,255,255,1) 0%,#b7e0f4 40%,#6cbbe8 100%)}
.back .splash{position:absolute;left:0;top:0;width:160px;height:80px;background:linear-gradient(120deg,#d4eefb,#8fcbee 60%,rgba(255,255,255,0));border-radius:0 0 60% 0}
.back .logo{left:240px;top:42px;font-size:30px;color:var(--blue)}
.back .mascot-top{left:500px;top:4px;width:80px;height:102px}
.grid{position:absolute;left:28px;top:112px;width:772px;display:grid;grid-template-columns:repeat(4,1fr);grid-template-rows:139px 261px;gap:6px 12px}
.box{border:1.5px solid var(--panel-line);border-radius:6px;overflow:hidden;background:var(--white)}
.box h4{background:var(--navy);color:var(--white);font-size:9px;font-weight:700;text-transform:uppercase;height:30px;display:flex;align-items:center;gap:7px;padding:0 9px;line-height:1.15}
.box h4 .hi{width:18px;height:18px;border-radius:50%;border:1.5px solid var(--white);flex:none}
.box .body{padding:7px 8px 5px 9px;font-size:7px;line-height:1.28}
.box ul{list-style:none;flex:1;min-width:0}
.box li{position:relative;padding-left:10px;margin-bottom:5px;font-weight:500}
.box li::before{content:"";position:absolute;left:0;top:1px;width:6px;height:6px;border-radius:50%;background:var(--red)}
.box li .sub{display:block;font-weight:400;color:var(--grey);font-size:5.8px;line-height:1.22;margin-top:1px}
.box li b{font-weight:700}
.notebox{margin-top:4px;background:var(--note);border-radius:4px;padding:4px 7px;font-size:6px;line-height:1.25;color:var(--navy);display:flex;gap:6px;align-items:center}
.notebox i{width:11px;height:11px;border-radius:50%;border:1px solid var(--navy);flex:none}
.svc{display:flex;gap:6px;margin-bottom:2px}
.svc .si{width:14px;height:14px;border:1.3px solid var(--blue);border-radius:3px;flex:none;margin-top:1px}
.info{display:flex;gap:8px;margin-bottom:3px}
.info .si{width:16px;height:16px;border:1.3px solid var(--blue);border-radius:50%;flex:none}
.back .mascot-bot{right:22px;top:440px;width:74px;height:86px;border-radius:40% 40% 6px 6px}
.back .footbar{height:41px;padding-left:40px}
.back .footbar .about{width:330px;font-size:6.3px;line-height:1.35}
</style>
</head>
<body>

<section class="card front" aria-label="Postcard front">
  <div class="scene" role="img" aria-label="Photo of a resort pool with palm trees under a blue sky"></div>
  <div class="headline-bg"></div>
  <h1 class="headline"><span class="l1">CLEAN POOLS.</span><span class="l2">CLEAR CHOICE.</span></h1>
  <div class="tagbar">RELIABLE SERVICE. CRYSTAL CLEAR RESULTS.</div>
  <div class="mascot mascot-top" role="img" aria-label="Illustrated pool technician mascot holding a skimmer net"></div>
  <div class="logo"><span class="dot"></span>Tide Sweepers</div>
  <div class="truck" role="img" aria-label="Illustration of a branded service pickup truck"></div>
  <div class="mascot mascot-left" role="img" aria-label="Illustrated pool technician mascot with arms crossed"></div>
  <div class="offer">
    <div class="lbl">NEW CUSTOMER<br>START-UP FEE</div>
    <div class="price"><sup>$</sup>85</div>
    <div class="note">Applies to all new service agreements.</div>
  </div>
  <div class="features">
    <div class="feature"><div class="ic"><svg width="18" height="18" viewBox="0 0 24 24"><path d="M12 2l8 3v6c0 5-3.5 9-8 11-4.5-2-8-6-8-11V5z" fill="none" stroke="#e8412c" stroke-width="2"/><path d="M8 12l3 3 5-6" fill="none" stroke="#e8412c" stroke-width="2"/></svg></div><h3>Reliable Service</h3><p>On-time, professional<br>&amp; dependable.</p></div>
    <div class="feature"><div class="ic"><svg width="18" height="18" viewBox="0 0 24 24"><path d="M12 2c4 5 7 9 7 13a7 7 0 0 1-14 0c0-4 3-8 7-13z" fill="none" stroke="#e8412c" stroke-width="2"/></svg></div><h3>Clear Water</h3><p>Balanced, safe and<br>sparkling every time.</p></div>
    <div class="feature"><div class="ic"><svg width="18" height="18" viewBox="0 0 24 24"><rect x="5" y="4" width="14" height="16" rx="2" fill="none" stroke="#e8412c" stroke-width="2"/><path d="M5 10h14M12 4v16" stroke="#e8412c" stroke-width="2"/></svg></div><h3>Expert Care</h3><p>Thorough filter cleaning &amp;<br>equipment inspection.</p></div>
    <div class="feature"><div class="ic"><svg width="18" height="18" viewBox="0 0 24 24"><circle cx="12" cy="9" r="4" fill="none" stroke="#e8412c" stroke-width="2"/><path d="M4 21c1-5 15-5 16 0" fill="none" stroke="#e8412c" stroke-width="2"/></svg></div><h3>Customer Focused</h3><p>Your satisfaction is<br>our top priority.</p></div>
  </div>
  <div class="strip"></div>
  <div class="footbar">
    <p class="about">At TIDE SWEEPERS, we provide professional pool and spa care so you can relax and enjoy your water worry-free.</p>
    <div class="contact"><svg class="ci" viewBox="0 0 24 24"><circle cx="12" cy="12" r="11" fill="none" stroke="#fff" stroke-width="1.6"/><path d="M8 7l2 0 1 3-1.5 1a7 7 0 0 0 3.5 3.5L14 13l3 1v2c-5 1-10-4-9-9z" fill="#fff"/></svg>619-555-0148</div>
    <div class="contact"><svg class="ci" viewBox="0 0 24 24"><circle cx="12" cy="12" r="10" fill="none" stroke="#fff" stroke-width="1.6"/><path d="M2 12h20M12 2c3 3 3 17 0 20M12 2c-3 3-3 17 0 20" fill="none" stroke="#fff" stroke-width="1.4"/></svg>www.tidesweepers.com</div>
  </div>
</section>

<section class="card back" aria-label="Postcard back">
  <div class="water" role="img" aria-label="Photo of a pool edge with clear blue water"></div>
  <div class="splash" role="img" aria-label="Water splash graphic"></div>
  <div class="logo"><span class="dot"></span>Tide Sweepers</div>
  <div class="mascot mascot-top" role="img" aria-label="Illustrated pool technician mascot with arms crossed"></div>

  <div class="grid">
    <div class="box"><h4><span class="hi"></span>Water Clarity and Quality Guarantee</h4><div class="body"><ul>
      <li>The Company ensures proper chemical balance to prevent algae and bacteria growth.</li>
      <li>Water clarity depends on three factors<span class="sub">· Chemical balance<br>· Filtration<br>· Circulation</span></li></ul>
      <div class="notebox"><i></i>The Company guarantees water clarity only as it pertains to chemistry.</div></div></div>
    <div class="box"><h4><span class="hi"></span>Exclusions</h4><div class="body"><ul>
      <li>Services do not include repairing or addressing structural damage, underground leaks, or equipment not maintained per industry standards.</li>
      <li>Missed visits due to inaccessible areas (e.g., locked gates or unremoved covers) will not be refunded or rescheduled.</li></ul></div></div>
    <div class="box"><h4><span class="hi"></span>Repairs &amp; Equipment Maintenance</h4><div class="body"><ul>
      <li>All repair requests will be evaluated, quoted, and approved by the Client before execution.</li>
      <li>Repairs related to county-mandated safety updates will be billed separately.</li></ul></div></div>
    <div class="box"><h4><span class="hi"></span>Liability</h4><div class="body"><ul>
      <li>TIDE SWEEPERS is not liable for pre existing conditions or equipment failures including but not limited to pumps, motors, filters, or pool structures.</li></ul></div></div>

    <div class="box"><h4><span class="hi"></span>Services Provided</h4><div class="body">
      <div class="svc"><span class="si"></span><ul><li><b>Basic Service</b><span class="sub">· Two visits per month.<br>· Diagnostic testing and adjustment for chlorine, pH, &amp; complete water balance.</span></li></ul></div>
      <div class="svc"><span class="si"></span><ul><li><b>Basic Plus Service</b><span class="sub">· Includes Basic Service, plus quarterly filter cleaning and an equipment evaluation.</span></li></ul></div>
      <div class="svc"><span class="si"></span><ul><li><b>Full Service</b><span class="sub">· No less than four visits per month.<br>· Chemical testing and balance, floating chlorinator maintenance, debris removal, wall and tile brushing, basket emptying, and filter cleaning (for filters under 200 sq.ft).</span></li></ul></div>
      <div class="svc"><span class="si"></span><ul><li><b>Extra Full Service</b><span class="sub">· Recommended for pools prone to heavy debris.<br>· Includes all Full Service offerings, with six visits per month for weekly cleanings and chemical treatments.</span></li></ul></div>
    </div></div>
    <div class="box"><h4><span class="hi"></span>Client Responsibilities</h4><div class="body"><ul>
      <li><b>Water Level</b><span class="sub">· Clients must maintain proper pool/spa/fountain water levels. In most cases, the skimmer opening should be submerged halfway underwater. Proper water level ensures effective filtration and chemical balance.</span></li>
      <li><b>Access &amp; Pool Preparation</b><span class="sub">· Clear, safe access to the pool area must be provided on the day of service.<br>· Pool toys, floating mats, and solar covers must be removed prior to service.<br>· Safety features, including nets or covers, must be removed before our visit. The Company will not remove or reinstall these items.<br>· Failure to prepare the pool area may result in incomplete service, and no reschedule or credit is guaranteed for such missed services.</span></li></ul></div></div>
    <div class="box"><h4><span class="hi"></span>Service Charges</h4><div class="body"><ul>
      <li>All new Customers are required to have an initial deep filter cleaning and complete equipment inspection.</li>
      <li>Additional filter cleanings will be performed on a scheduled basis, or as needed, at an additional charge.</li>
      <li>Replacement cartridges, grids, &amp; other filter parts will be replaced as needed at an additional charge.</li>
      <li>Any request deemed as service calls, repairs, and evaluations are at an additional charge</li></ul>
      <div class="notebox"><i></i>Any request deemed as service calls, repairs, and evaluations are at an additional charge</div></div></div>
    <div class="box"><h4><span class="hi"></span>Additional Information</h4><div class="body">
      <div class="info"><span class="si"></span><ul><li><b>Safety</b><span class="sub">Swimming is safe 30 minutes after chemical treatment.</span></li></ul></div>
      <div class="info"><span class="si"></span><ul><li><b>On-Site Records</b><span class="sub">Service records will be kept in the pool's timer box and service logs left at the property.</span></li></ul></div>
      <div class="info"><span class="si"></span><ul><li><b>Initial Start-Up Fee</b><span class="sub">$85 applies to all new service agreements</span></li></ul></div>
      <div class="info"><span class="si"></span><ul><li><b>Service Changes</b><span class="sub">Service terms and rates are subject to change with 30 days' notice.</span></li></ul></div>
    </div></div>
  </div>
  <div class="mascot mascot-bot" role="img" aria-label="Illustrated pool technician mascot giving a thumbs up"></div>

  <div class="footbar">
    <p class="about">The service plan includes either 48 or 24 scheduled visits based on a 52-week year, with service pauses during the week of Thanksgiving, Easter, Christmas, and a fourth week at our discretion, with prior notification. Prior to any pause in service, we will take measures to maintain water quality before each scheduled break.</p>
    <div class="contact"><svg class="ci" viewBox="0 0 24 24"><circle cx="12" cy="12" r="11" fill="none" stroke="#fff" stroke-width="1.6"/><path d="M8 7l2 0 1 3-1.5 1a7 7 0 0 0 3.5 3.5L14 13l3 1v2c-5 1-10-4-9-9z" fill="#fff"/></svg>619-555-0148</div>
    <div class="contact"><svg class="ci" viewBox="0 0 24 24"><circle cx="12" cy="12" r="10" fill="none" stroke="#fff" stroke-width="1.6"/><path d="M2 12h20M12 2c3 3 3 17 0 20M12 2c-3 3-3 17 0 20" fill="none" stroke="#fff" stroke-width="1.4"/></svg>www.tidesweepers.com</div>
  </div>
</section>

</body>
</html>
```